Business card for Mortgage broker business

I have already had the logo designed and am needing a great looking business card. My business focus is on servicing clients who may not be able to obtain finance through traditional lenders due to bad credit, short term employment or they just don't fit the banks profile. It needs to be professional, trust worthy but also have a caring fell about it.
I have provided files showing the green and black logo, the white logo(on white background so the file looks blank) and also a file with the white logo with a background of leaves that was made up which will probably be used for a website header.

Industry/Entity Type

Finance

Contact Information for Business Card

Marcus Dolbey
Managing Director, Accredited Finance Broker(AFB)
Po Box 287, Pakenham VIC 3810
marcus@kestrelfinance.com.au
www.kestrelfinance.com.au
0438 162 507

Requirements
Nice to have
• I have added a picture of myself as I would like to see some designs with the pic in it, but I'm not sure if I want it on there with the logo's or just the logo's

```html
<!DOCTYPE html>
<html lang="en">
<head>
<meta charset="utf-8">
<title>Kestrel Finance — Business Card</title>
<link href="https://fonts.googleapis.com/css2?family=Roboto+Slab:wght@300;400&display=swap" rel="stylesheet">
<style>
  :root {
    --backdrop: #ececec;
    --card-white: #f7f7f7;
    --brand-green: #3f8a57;
    --ink: #3a3a3a;
    --leaf-red: #8e1f2c;
    --leaf-crimson: #b8313a;
    --leaf-amber: #c98a3a;
    --leaf-tan: #d9b27a;
    --leaf-shadow: #4a1118;
    --white: #ffffff;
  }
  html, body {
    margin: 0;
    padding: 0;
    width: 1200px;
    height: 1000px;
    overflow: hidden;
    background: var(--backdrop);
    font-family: "Roboto Slab", Georgia, serif;
  }
  .canvas {
    position: relative;
    width: 1200px;
    height: 1000px;
  }
  .card {
    position: absolute;
    left: 330px;
    width: 540px;
    height: 300px;
    box-shadow: 0 10px 28px rgba(0,0,0,0.18);
    overflow: hidden;
  }
  .card-front { top: 160px; }
  .card-back  { top: 540px; background: var(--card-white); }

  .leaf-photo {
    position: absolute;
    inset: 0;
    background:
      radial-gradient(ellipse at 70% 25%, var(--leaf-tan) 0%, transparent 45%),
      radial-gradient(ellipse at 55% 55%, var(--leaf-amber) 0%, transparent 50%),
      radial-gradient(ellipse at 20% 75%, var(--leaf-crimson) 0%, transparent 55%),
      linear-gradient(135deg, var(--leaf-red) 0%, var(--leaf-crimson) 35%, var(--leaf-amber) 65%, var(--leaf-shadow) 100%);
  }
  .front-wordmark {
    position: absolute;
    left: 0;
    right: 0;
    top: 118px;
    text-align: center;
    color: var(--white);
    font-weight: 400;
    font-size: 44px;
    letter-spacing: 1px;
  }

  .back-wordmark {
    position: absolute;
    left: 36px;
    top: 128px;
    display: flex;
    align-items: center;
    gap: 8px;
    color: var(--brand-green);
    font-weight: 400;
    font-size: 22px;
  }
  .back-wordmark .dot {
    width: 10px;
    height: 10px;
    border-radius: 50%;
    background: var(--brand-green);
  }
  .divider {
    position: absolute;
    left: 262px;
    top: 100px;
    width: 2px;
    height: 150px;
    background: var(--brand-green);
  }
  .contact {
    position: absolute;
    left: 286px;
    top: 44px;
    color: var(--ink);
    font-weight: 300;
  }
  .contact .name {
    font-size: 24px;
    margin: 0;
    line-height: 1.1;
  }
  .contact .role {
    font-size: 15px;
    color: var(--brand-green);
    letter-spacing: 0.5px;
    margin: 2px 0 22px;
  }
  .contact .details {
    margin: 0;
    padding: 0;
    list-style: none;
    font-size: 16px;
    line-height: 1.18;
  }
</style>
</head>
<body>
  <main class="canvas">
    <section class="card card-front">
      <div class="leaf-photo" role="img" aria-label="Close-up photograph of red, orange and golden autumn maple leaves"></div>
      <div class="front-wordmark">Kestrel Finance</div>
    </section>

    <section class="card card-back">
      <div class="back-wordmark"><span class="dot"></span><span>Kestrel Finance</span></div>
      <div class="divider"></div>
      <div class="contact">
        <p class="name">John Doe</p>
        <p class="role">SALES MANAGER</p>
        <ul class="details">
          <li>www.website.com</li>
          <li>hello@email.com</li>
          <li>123 456 7890</li>
          <li>123 Street</li>
          <li>City, State, Country</li>
        </ul>
      </div>
    </section>
  </main>
</body>
</html>
```